Brightway Inc. Business Card Design

Brightway Inc. is in search of a great clean design for our business cards!

Looking to incorporate our full logo and watermark on side one (however, I am open to having the text and watermark separated within the design.)

On side two, I am looking to have contact information (Name, Position, Phone #, Email, Website (www.thebrightway.ca). Can have the logo and/or watermark as part of the design if applicable.

Please add tagline "Where Shine Counts" on either side 1 or 2. This tagline can be in a sans serif, serif or cursive font as long as it compliments overall design. Capitalization can be title or sentence case depending on how it fits within the design.

Get creative!! Looking for a clean, crisp, premium design! Looking for a glossy card finish with spot UV features when printed. Cards will also be printed with rounded corners. Standard dimensions (3.5 x 2).

Target Market(s)

B2B - primary clients are business owners or property management corporations. (residential jobs are few and far between)

Industry/Entity Type

Business

Contact Information for Business Card

- clean, crisp design
- double sided
- spot UV accents and glossy finish upon printing
- standard business card size (3.5 x 2) with rounded corners
- please see project description for requirements per side

Font styles to use
Sans Serif

Requirements
Must have
• - adequate bleeds with print ready files
• - cohesive design elements between side 1 & 2
• - spot UV elements (can be on both sides or just one, use your discretion)
• - colour pallet should match the logo file provided
• - incorporate tagline "where shine counts" (this tagline can be in a serif or sans serif font as long as it is complimentary to the overall design.
Nice to have
• - Premium elements with a clean design
Should not have
• - Please omit cartoon or whimsical like designs, think premium.
• - Colours should not stray from the pallet of the provided logo.

```html
<!DOCTYPE html>
<html lang="en">
<head>
<meta charset="UTF-8">
<title>Brightway Inc. Business Card</title>
<link rel="stylesheet" href="https://fonts.googleapis.com/css2?family=Work+Sans:wght@400;500;700&family=Oswald:wght@600&display=swap">
<style>
  :root {
    --backdrop: #2a2b2e;
    --navy: #1d2762;
    --navy-light: #2a3780;
    --teal: #27bcbf;
    --silver: #a9aebb;
    --rule: #8d96c4;
    --white: #ffffff;
  }
  * { margin: 0; padding: 0; box-sizing: border-box; }
  html, body {
    width: 1200px; height: 900px; overflow: hidden;
    background: var(--backdrop);
    font-family: "Work Sans", sans-serif;
  }
  .canvas { position: relative; width: 1200px; height: 900px; }
  .card {
    position: absolute; left: 250px; width: 700px; height: 400px;
    border-radius: 14px; overflow: hidden;
    box-shadow: 0 10px 28px rgba(0,0,0,0.45);
  }
  /* Side one */
  .card-front {
    top: 40px;
    background: linear-gradient(160deg, var(--navy-light) 0%, var(--navy) 70%);
  }
  .front-wordmark {
    position: absolute; top: 140px; left: 0; right: 0;
    display: flex; justify-content: center; align-items: center; gap: 18px;
  }
  .front-wordmark .mark-square {
    width: 46px; height: 46px; background: var(--silver); opacity: 0.55;
  }
  .front-wordmark .name {
    font-weight: 700; font-size: 58px; letter-spacing: -1px;
    color: var(--silver);
  }
  .tagline-row {
    position: absolute; top: 292px; left: 0; right: 0;
    display: flex; align-items: center; gap: 14px; padding: 0 0;
  }
  .tagline-row .rule { flex: 1; height: 1px; background: var(--rule); }
  .tagline {
    font-size: 17px; letter-spacing: 3px; text-transform: uppercase;
    color: var(--white); font-weight: 400;
  }
  /* Side two */
  .card-back { top: 470px; background: var(--white); }
  .back-wordmark {
    position: absolute; top: 52px; left: 0; right: 0;
    display: flex; justify-content: center; align-items: center; gap: 14px;
  }
  .back-wordmark .mark-square { width: 34px; height: 34px; background: var(--teal); }
  .back-wordmark .name {
    font-weight: 700; font-size: 44px; letter-spacing: -1px; color: var(--navy);
  }
  .person {
    position: absolute; top: 168px; left: 95px; width: 215px; text-align: right;
  }
  .person-name {
    font-family: "Oswald", sans-serif; font-weight: 600; font-size: 40px;
    line-height: 1; color: var(--navy); letter-spacing: 0.5px;
  }
  .person-role {
    margin-top: 6px; font-size: 15px; font-weight: 500;
    letter-spacing: 2px; color: var(--teal);
  }
  .divider {
    position: absolute; top: 170px; left: 340px; width: 1.5px; height: 58px;
    background: var(--navy);
  }
  .contacts {
    position: absolute; top: 166px; left: 368px; list-style: none;
  }
  .contacts li {
    display: flex; align-items: center; gap: 12px;
    font-size: 17px; line-height: 22px; color: var(--teal);
  }
  .contacts svg { width: 13px; height: 13px; flex: none; }
  .address {
    position: absolute; top: 300px; left: 95px;
    font-size: 18px; color: var(--teal); letter-spacing: 0.3px;
  }
</style>
</head>
<body>
<main class="canvas">
  <section class="card card-front" aria-label="Business card, side one">
    <div class="front-wordmark">
      <span class="mark-square"></span>
      <span class="name">BRIGHTWAY INC.</span>
    </div>
    <div class="tagline-row">
      <span class="rule"></span>
      <span class="tagline">Where Shine Counts</span>
      <span class="rule"></span>
    </div>
  </section>

  <section class="card card-back" aria-label="Business card, side two">
    <div class="back-wordmark">
      <span class="mark-square"></span>
      <span class="name">BRIGHTWAY INC.</span>
    </div>
    <div class="person">
      <div class="person-name">MARCUS HALE</div>
      <div class="person-role">DIRECTOR</div>
    </div>
    <div class="divider"></div>
    <ul class="contacts">
      <li>
        <svg viewBox="0 0 16 16" aria-hidden="true"><path d="M4 1l3 3-2 2c1 2 3 4 5 5l2-2 3 3-2 3C7 15 1 9 1 3z" fill="var(--navy)"/></svg>
        905-555-0147
      </li>
      <li>
        <svg viewBox="0 0 16 16" aria-hidden="true"><rect x="1.5" y="3.5" width="13" height="9" fill="none" stroke="var(--navy)" stroke-width="1.4"/><path d="M1.5 3.5L8 9l6.5-5.5" fill="none" stroke="var(--navy)" stroke-width="1.4"/></svg>
        info@brightwayservices.ca
      </li>
      <li>
        <svg viewBox="0 0 16 16" aria-hidden="true"><circle cx="8" cy="8" r="6.5" fill="none" stroke="var(--navy)" stroke-width="1.3"/><ellipse cx="8" cy="8" rx="2.8" ry="6.5" fill="none" stroke="var(--navy)" stroke-width="1.1"/><path d="M1.5 8h13" stroke="var(--navy)" stroke-width="1.1"/></svg>
        www.thebrightway.ca
      </li>
    </ul>
    <p class="address">480 Harbour Road Suite 210 Lakeview ON L4K 2M5.</p>
  </section>
</main>
</body>
</html>
```